One name card with 4 companies logos

Hi, I would like to have a design of name card with my 4 companies logos incorporated into a single, 2-sided name card.

Information for name card:
1. Slogan "Transforming Lives"
2. Critical info: "Name", "Role", "Mobile Number", "Email", "Website"
3. Please follow the sequence in placing the logos (DVX, KRPE, Brivoquest, Nevo Foundation)

Page 1 of namecard - 4 Company Logos
Page 2 of namecard - Transforming Lives + Namecard information

B2B - Companies and government bodies

4. Please put this in the page 2 of card:
Accredited Training Provider
(7 logos/icons of different brands)

Designer to choose colors to be used in the design.

• Use white as a base color for namecard

```html
<!DOCTYPE html>
<html lang="en">
<head>
<meta charset="utf-8">
<title>DVX Name Card</title>
<link href="https://fonts.googleapis.com/css2?family=Poppins:wght@400;500;700&display=swap" rel="stylesheet">
<style>
  :root{
    --backdrop:#8d8b8c;
    --gold:#c99c2c;
    --white:#ffffff;
    --navy:#2b3f94;
    --ink:#333333;
    --muted:#8a8a8a;
    --badge:#d9d9d9;
    --red:#e3262b;
    --yellow:#efe21f;
    --green:#24834a;
    --blue:#0d5a94;
    --leaf:#3aa84a;
    --black:#111111;
  }
  *{margin:0;padding:0;box-sizing:border-box}
  html,body{width:1200px;height:900px;overflow:hidden}
  body{
    background:var(--backdrop);
    font-family:"Poppins",sans-serif;
    display:flex;flex-direction:column;align-items:center;justify-content:center;gap:44px;
  }
  .card{
    width:640px;height:366px;position:relative;
    box-shadow:0 8px 18px rgba(0,0,0,.28);
  }
  .card-back{background:var(--gold);display:flex;align-items:center;justify-content:center}
  .brand-mark{font-weight:700;letter-spacing:4px;line-height:1}
  .card-back .brand-mark{color:var(--white);font-size:104px}
  .card-front{background:var(--white);overflow:hidden}
  .brand-block{position:absolute;top:30px;right:48px;text-align:right}
  .card-front .brand-mark{color:var(--gold);font-size:66px}
  .slogan{margin-top:6px;color:var(--navy);font-size:12px;font-weight:500;letter-spacing:2px;text-transform:uppercase}
  .identity{position:absolute;left:40px;top:138px}
  .identity-name{color:var(--navy);font-weight:700;font-size:26px;line-height:1.1;letter-spacing:.5px}
  .identity-role{color:var(--ink);font-weight:500;font-size:16px;letter-spacing:.5px}
  .accreditation{position:absolute;right:48px;top:150px;text-align:right}
  .accreditation-label{font-size:10px;font-weight:500;color:var(--muted);letter-spacing:1px;text-transform:uppercase;margin-bottom:6px}
  .accreditation-badges{display:flex;gap:7px;justify-content:flex-end}
  .badge{width:24px;height:24px;background:var(--badge);border-radius:4px}
  .badge.round{border-radius:50%}
  .contacts{position:absolute;left:40px;bottom:50px;list-style:none}
  .contact{display:flex;align-items:center;gap:14px;font-size:15px;color:var(--ink);line-height:1.7;letter-spacing:.3px}
  .contact svg{width:16px;height:16px;flex:none}
  .contact .accent{color:var(--gold)}
  .partners{position:absolute;right:26px;bottom:38px;display:flex;align-items:flex-end;gap:24px}
  .partner{display:flex;align-items:center;gap:6px;font-weight:700;line-height:1}
  .partner-dot{display:inline-block;border-radius:50%}
  .partner-krpe{color:var(--black);font-size:17px}
  .partner-krpe .partner-dot{width:14px;height:14px;background:var(--red)}
  .partner-brivo{color:var(--leaf);font-size:16px}
  .partner-brivo .partner-dot{width:16px;height:16px;background:var(--navy)}
  .partner-nevo{color:var(--leaf);font-size:8px;flex-direction:column;gap:3px;font-weight:500}
  .partner-nevo .partner-dot{width:20px;height:20px;border:2px solid var(--leaf)}
  .color-band{position:absolute;left:0;right:0;bottom:0;height:18px;display:flex}
  .color-band span{flex:1}
  .band-red{background:var(--red)}
  .band-yellow{background:var(--yellow)}
  .band-green{background:var(--green)}
  .band-blue{background:var(--blue)}
</style>
</head>
<body>
  <section class="card card-back">
    <div class="brand-mark">DVX</div>
  </section>

  <section class="card card-front">
    <div class="brand-block">
      <div class="brand-mark">DVX</div>
      <div class="slogan">Transforming Lives</div>
    </div>

    <div class="identity">
      <div class="identity-name">ARLEN VOSS</div>
      <div class="identity-role">FOUNDER</div>
    </div>

    <div class="accreditation">
      <div class="accreditation-label">Accredited Training Provider</div>
      <div class="accreditation-badges">
        <span class="badge"></span>
        <span class="badge round"></span>
        <span class="badge"></span>
        <span class="badge round"></span>
        <span class="badge"></span>
        <span class="badge round"></span>
        <span class="badge"></span>
      </div>
    </div>

    <ul class="contacts">
      <li class="contact">
        <svg viewBox="0 0 16 16"><path d="M4 2l2.5 3-1.5 1.5c.8 1.8 2.2 3.2 4 4L10.5 9l3 2.5-1.5 2c-5 0-10-5-10-10z" fill="var(--navy)"/></svg>
        <span>(123)456-7890</span>
      </li>
      <li class="contact">
        <svg viewBox="0 0 16 16"><rect x="1" y="3" width="14" height="10" fill="var(--red)"/><path d="M1 3l7 6 7-6" fill="none" stroke="var(--white)" stroke-width="1.4"/></svg>
        <span>info@arlenvoss.com</span>
      </li>
      <li class="contact">
        <svg viewBox="0 0 16 16"><circle cx="6.5" cy="6.5" r="4.5" fill="none" stroke="var(--leaf)" stroke-width="2.2"/><path d="M10 10l4.5 4.5" stroke="var(--leaf)" stroke-width="2.6" stroke-linecap="round"/></svg>
        <span>www.<span class="accent">yoursite</span>.com</span>
      </li>
    </ul>

    <div class="partners">
      <div class="partner partner-krpe"><span class="partner-dot"></span>KRPE</div>
      <div class="partner partner-brivo"><span class="partner-dot"></span>Brivoquest.com</div>
      <div class="partner partner-nevo"><span class="partner-dot"></span>Nevo Foundation</div>
    </div>

    <div class="color-band">
      <span class="band-red"></span>
      <span class="band-yellow"></span>
      <span class="band-green"></span>
      <span class="band-blue"></span>
    </div>
  </section>
</body>
</html>
```